Guitar parts retail packaging

I have 2 boxes I need designed. This will be for my guitar parts. They are going to be thick cardstock type paper box, with a foam insert to secure the items. Matte finish with silver foil printing is sort of where im headed, but Im open to other beautiful design. The boxes will need to have a window on top of the box to show the product inside. Color scheme Im thinking with is Black with red, white and Silver foil printing. Unless you come up with something nicer, im open to that. But my business cards and some stickers are those colors.
2 different size boxes, but they can be the same basic design, modified for 2 different sizes. They will open at the front, and the lid will lift, hinged at the top back edge. (Please see purple box in picture for example for how box will work). Both boxes will have a window on top to showcase product in the box. One of the sides, (2" X 1.25") will be left a solid color, grey or other so I can put a product sticker on that side to designate what type of product is in the box. So you are really just designing the top (With window), front, back, and 1 side. Maybe something clever on the bottom but if thats blank thats fine.
LARGE BOX:
5.25 wide (Left to right)
2” deep (Front to back)
1.25” tall (Top to bottom)
SMALL BOX:
2” Wide (Left to right)
2” Deep (Front to back)
Please see Business card and sticker in picture for color scheme Im thinking. ( I am open to other colors and designs as well)

Target Market(s)

Musicians, Rockers, tattoo junkies, general badasses.

Industry/Entity Type

Guitar industry. Rock & Rollers

Font styles to use
Other font styles liked:
• I use a font called Morpheus for my logo. Also Times New Roman, maybe Copperplate? Or something more creative? Im open as long as it fits.

Colors
EB3D1F
EC4F4E
F09395
F8D3D4
FCEDEE

Requirements
Must have
• My Company name and logo (Harrow Kestrel). Also slogan-
Nice to have
• Please see general aesthetic in sticker and biz card.
Should not have
• No horror themes, keep it cool and classy. (Even though logo is a skull). And please no pictures of guitars on the box. You might add a pic of 1 type of guitar, but the parts inside might not fit that guitar pictured on the box.

```html
<!DOCTYPE html>
<html lang="en">
<head>
<meta charset="utf-8">
<title>Harrow Kestrel – Guitar Parts Box Dielines</title>
<link rel="stylesheet" href="https://fonts.googleapis.com/css2?family=Cinzel:wght@600&display=swap">
<style>
  :root {
    --page: #ffffff;
    --board-dark: #0d0d10;
    --board-mid: #1d1d23;
    --silver: #e9e9ea;
    --window: #a9a9ab;
    --ornament: #6e1c16;
    --cut: #c8c21e;
    --fold: #d9252b;
  }
  html, body {
    margin: 0;
    padding: 0;
    width: 720px;
    height: 1200px;
    overflow: hidden;
    background: var(--page);
  }
  .canvas {
    display: block;
    width: 720px;
    height: 1200px;
  }
  .panel { fill: url(#boardFill); }
  .wordmark {
    font-family: "Cinzel", serif;
    font-weight: 600;
    fill: var(--silver);
  }
  .ornament { fill: var(--ornament); opacity: 0.55; }
  .guitar-window { fill: var(--window); }
  .product-window { fill: url(#windowFill); }
  .cut-line { fill: none; stroke: var(--cut); stroke-width: 2; stroke-dasharray: 8 5; }
  .fold-line { fill: none; stroke: var(--fold); stroke-width: 2; }
  .thumb-notch { fill: var(--page); }
</style>
</head>
<body>
<svg class="canvas" viewBox="0 0 1484 2474" xmlns="http://www.w3.org/2000/svg">
  <defs>
    <linearGradient id="boardFill" x1="0" y1="0" x2="1" y2="1">
      <stop offset="0" stop-color="var(--board-mid)"/>
      <stop offset="1" stop-color="var(--board-dark)"/>
    </linearGradient>
    <linearGradient id="windowFill" x1="0" y1="0" x2="1" y2="0">
      <stop offset="0" stop-color="#9c9c9e"/>
      <stop offset="0.5" stop-color="#d4d4d6"/>
      <stop offset="1" stop-color="#a4a4a6"/>
    </linearGradient>

    <g id="boxNet">
      <!-- lid -->
      <path class="panel" d="M90,1315 V1185 Q90,1158 117,1158 H550 Q577,1158 577,1185 V1315 Z"/>
      <!-- front band running across the net -->
      <rect class="panel" x="48" y="1315" width="1387" height="115"/>
      <!-- side flaps -->
      <path class="panel" d="M605,1200 H735 Q757,1200 757,1222 Q757,1290 762,1315 V1430 Q757,1455 757,1523 Q757,1545 735,1545 H605 Q583,1545 583,1523 Q583,1455 577,1430 V1315 Q583,1290 583,1222 Q583,1200 605,1200 Z"/>
      <path class="panel" d="M1277,1200 H1408 Q1430,1200 1430,1222 Q1430,1290 1435,1315 V1430 Q1430,1455 1430,1523 Q1430,1545 1408,1545 H1277 Q1255,1545 1255,1523 Q1255,1455 1250,1430 V1315 Q1255,1290 1255,1222 Q1255,1200 1277,1200 Z"/>
      <!-- base -->
      <path class="panel" d="M762,1430 H1250 V1560 Q1250,1587 1223,1587 H789 Q762,1587 762,1560 Z"/>

      <!-- front wordmark with ornament bands -->
      <rect class="ornament" x="240" y="1322" width="180" height="16" rx="8" role="img" aria-label="Red flourish ornament"/>
      <text class="wordmark" x="332" y="1390" text-anchor="middle" font-size="38">Harrow Kestrel</text>
      <rect class="ornament" x="240" y="1402" width="180" height="16" rx="8" role="img" aria-label="Red flourish ornament"/>

      <!-- back wordmark -->
      <rect class="ornament" x="920" y="1322" width="180" height="16" rx="8" role="img" aria-label="Red flourish ornament"/>
      <text class="wordmark" x="1010" y="1388" text-anchor="middle" font-size="38">Harrow Kestrel</text>
      <rect class="ornament" x="920" y="1402" width="180" height="16" rx="8" role="img" aria-label="Red flourish ornament"/>

      <!-- side name marks -->
      <text class="wordmark" x="670" y="1366" text-anchor="middle" font-size="22">Harrow</text>
      <text class="wordmark" x="670" y="1396" text-anchor="middle" font-size="22">Kestrel</text>
      <text class="wordmark" x="1343" y="1366" text-anchor="middle" font-size="22">Harrow</text>
      <text class="wordmark" x="1343" y="1396" text-anchor="middle" font-size="22">Kestrel</text>
    </g>
  </defs>

  <!-- Large box net: guitar-shaped lid window -->
  <g class="net net-guitar" transform="translate(0,-620)">
    <use href="#boxNet"/>
    <rect class="guitar-window" x="130" y="1205" width="410" height="100" rx="40" role="img" aria-label="Silver guitar-shaped window cut-out in the lid"/>
  </g>

  <!-- Large box net: rectangular lid window with cut and fold lines -->
  <g class="net net-window" transform="translate(-4,354)">
    <use href="#boxNet"/>
    <rect class="product-window" x="147" y="1224" width="369" height="67"/>
    <!-- fold lines -->
    <rect class="fold-line" x="49" y="1314" width="1390" height="115"/>
    <line class="fold-line" x1="90" y1="1314" x2="90" y2="1429"/>
    <line class="fold-line" x1="577" y1="1314" x2="577" y2="1429"/>
    <line class="fold-line" x1="762" y1="1314" x2="762" y2="1429"/>
    <line class="fold-line" x1="1249" y1="1314" x2="1249" y2="1429"/>
    <!-- cut / crease lines -->
    <path class="cut-line" d="M90,1315 V1185 Q90,1158 117,1158 H550 Q577,1158 577,1185 V1315"/>
    <line class="cut-line" x1="90" y1="1198" x2="577" y2="1198"/>
    <path class="cut-line" d="M583,1315 Q583,1290 583,1222 Q583,1200 605,1200 H735 Q757,1200 757,1222 Q757,1290 762,1315"/>
    <path class="cut-line" d="M577,1430 Q583,1455 583,1523 Q583,1545 605,1545 H735 Q757,1545 757,1523 Q757,1455 762,1430"/>
    <path class="cut-line" d="M1255,1315 Q1255,1290 1255,1222 Q1255,1200 1277,1200 H1408 Q1430,1200 1430,1222 Q1430,1290 1435,1315"/>
    <path class="cut-line" d="M1250,1430 Q1255,1455 1255,1523 Q1255,1545 1277,1545 H1408 Q1430,1545 1430,1523 Q1430,1455 1435,1430"/>
    <path class="cut-line" d="M762,1430 V1560 Q762,1587 789,1587 H1223 Q1250,1587 1250,1560 V1430"/>
    <line class="cut-line" x1="762" y1="1546" x2="1250" y2="1546"/>
    <path class="thumb-notch" d="M1002,1315 A14,14 0 0 0 1030,1315 Z"/>
  </g>
</svg>
</body>
</html>
```